Help Give House Painter “Fresh” Website Makeover!

A residential and commercial painting company based in Albuquerque, NM, USA needs a fresh, new, fun, and playful--yet, simple, elegant and professional--website made.

Here is a link to their existing site:

http://corvelhomecoat.com/

We want to keep a similar site structure., So the navigation layout will stay the same. However, the video is too small, is too far over in the sidebar, and the overall design is amateur at best. We want something bright, colorful and bold!

We will need a space for the Video above the fold, and there needs to be space in the design for Testimonials, Specials and Images. It’s also very important to have the Angie’s List awards that you see on his current website.

Please also include somewhere in the Design icons for YouTube, Facebook, Google+ and LinkedIn.

Here are some examples to look at to get your creative juices flowing!

http://quillbrushworks.com/

http://www.tmvr.org/

http://www.marlowe-tasker.com/

http://www.plumtreepages.com/painting-company-plumtree-page/

http://www.quarrylanedesk.com/website-templates/painting-company-website-template-81735.html

We have accounts at both gleamvault.com and pixorra.com. If you use placeholder images from there, that's fine. We can buy the images when and if your design is selected.

Target Market(s)

The audience is the average middle class homeowner to higher upper class. This should appeal to families, couples, and singles who own a home.

Industry/Entity Type

Residential

Font styles to use
Sans Serif

Requirements
Must have
• - - Lots of color! It's a site about painting homes. People like a variety of colors. Bring out your inner artist, and get bold with your colors!

- - A video place holder. As you can see, there is a video on the existing site, but it's small and hidden. Make it big and put it top left, or in the center.

- -Detailed and organized PSD structure. We're going to turn your design into a website, and to make that work soothly, we ask that you organize you PSD well: name your layers, keep things separated, group and ungroup as necessary, etc.

- A sidebar that goes down the right side of an interior page. We need a homepage, and also one [1] interior page template. We don't need you to make a design for each page. Just the homepage, followed by a simple interior page design that requires only the header/navigation, and a sidebar down the right side.
Should not have
• - Coding. This is a design project only.

```html
<!DOCTYPE html>
<html lang="en">
<head>
<meta charset="utf-8">
<title>Corvel Painting – Albuquerque House Painters</title>
<link href="https://fonts.googleapis.com/css2?family=Open+Sans:wght@400;600;700;800&family=Oswald:wght@500;700&display=swap" rel="stylesheet">
<style>
:root{
  --red:#d8262b;
  --dark:#2f3033;
  --nav:#3a3b3e;
  --ink:#333;
  --muted:#6b6b6b;
  --cream:#f3efe6;
  --teal:#1aa3b8;
  --green:#6cb33f;
  --orange:#f08a1c;
  --pink:#e9569a;
  --gold:#f5a623;
  --light:#ececec;
  --white:#fff;
}
*{box-sizing:border-box;margin:0;padding:0}
html,body{width:1200px;height:2716px;overflow:hidden}
body{font-family:"Open Sans",Arial,sans-serif;color:var(--ink);background:var(--white);position:relative}
.abs{position:absolute}
.head-font{font-family:"Oswald","Arial Narrow",sans-serif;text-transform:uppercase;letter-spacing:.5px}

/* header */
.site-header{left:0;top:0;width:1200px;height:136px;background:linear-gradient(#fbfaf7,#f1eee8)}
.brand{left:56px;top:44px;display:flex;align-items:center;gap:12px}
.brand-mark{width:22px;height:22px;background:var(--red)}
.brand-name{font-size:34px;font-weight:700;color:var(--dark);line-height:1}
.header-phone{left:600px;top:50px;font-size:34px;font-weight:700;color:var(--dark);display:flex;align-items:center;gap:12px}
.award{top:14px;width:78px;height:96px;border-radius:8px 8px 40px 40px;background:linear-gradient(#8dc63f,#4f8f25)}
.award.a1{left:960px}.award.a2{left:1060px}
.main-nav{left:0;top:136px;width:1200px;height:40px;background:var(--nav);display:flex;align-items:center;padding-left:116px;gap:26px}
.main-nav a{color:var(--white);font-size:15px;font-weight:600;text-decoration:none;text-transform:uppercase}
.main-nav a.active{color:var(--gold)}

/* hero */
.hero{left:0;top:176px;width:1200px;height:684px;background:linear-gradient(160deg,#bcd8ec 0%,#e9a35a 45%,#b5472b 75%,#6e5a45 100%)}
.hero-copy{left:116px;top:210px;width:560px}
.hero-title{display:flex;align-items:center;gap:12px;white-space:nowrap}
.hero-title-text{font-size:38px;font-weight:800;color:var(--dark);line-height:1}
.hero-phone{background:var(--red);color:var(--white);font-size:32px;font-weight:800;padding:2px 12px;line-height:1.2}
.hero-sub{font-size:18px;font-weight:600;color:var(--dark);margin-top:14px;line-height:1.35;width:440px}

/* section backdrop */
.cream{left:0;top:860px;width:1200px;height:560px;background:var(--cream)}

/* feature cards */
.card{top:700px;width:296px;height:340px;background:var(--white);box-shadow:0 4px 10px rgba(0,0,0,.18)}
.card-title{height:64px;color:var(--white);font-size:21px;padding:8px 14px;line-height:1.1}
.card-img{height:130px}
.card-text{font-size:13px;color:var(--muted);padding:12px 14px 6px;line-height:1.5}
.card-more{font-size:12px;font-weight:700;padding:0 14px;color:var(--dark)}
.c1{left:100px}.c1 .card-title{background:var(--teal)}.c1 .card-img{background:linear-gradient(#c9dbe4,#8aa7b5)}
.c2{left:452px}.c2 .card-title{background:var(--green)}.c2 .card-img{background:linear-gradient(#e6d6b8,#b48c5a)}
.c3{left:804px}.c3 .card-title{background:var(--orange)}.c3 .card-img{background:linear-gradient(#e8d2be,#b39374)}

/* services */
.services{left:100px;top:1110px;width:1000px;display:flex}
.service{width:250px;text-align:center;padding:0 16px}
.service-icon{width:96px;height:96px;border-radius:50%;margin:0 auto;display:flex;align-items:center;justify-content:center}
.service h3{font-size:20px;margin-top:18px;color:var(--dark);line-height:1.2}
.service p{font-size:13px;color:var(--muted);margin-top:10px;line-height:1.5}

.rule{left:40px;top:1440px;width:1120px;height:2px;background:#d8d4cc}

/* about / video / specials */
.about{left:40px;top:1474px;width:340px}
.section-h{font-size:21px;color:var(--dark);line-height:1.2}
.about p{font-size:13px;color:var(--muted);line-height:1.6;margin-top:14px}
.videos{left:410px;top:1474px;width:480px}
.video-box{margin-top:16px;width:360px;height:230px;background:linear-gradient(#5a4a3c,#2b2420);position:relative}
.play{position:absolute;left:150px;top:85px}
.specials{left:920px;top:1484px;width:252px;height:270px;background:linear-gradient(135deg,#f6b13a,#e6781a);padding:24px;color:var(--white)}
.specials .sp-name{font-size:30px;font-weight:700;line-height:1.05}
.specials .sp-text{font-size:24px;font-weight:800;margin-top:70px;line-height:1.1}

/* testimonials */
.testi-h{left:0;top:1780px;width:1200px;text-align:center;font-size:30px;color:var(--dark)}
.testi{top:1850px;width:360px}
.t1{left:40px}.t2{left:420px}.t3{left:800px}
.quote{background:var(--white);border:1px solid #ddd;padding:20px 22px;font-size:13px;color:var(--muted);line-height:1.6;height:170px}
.rating{display:flex;align-items:center;gap:10px;margin-top:14px;padding-left:22px;font-size:14px;color:var(--ink)}
.stars{color:var(--gold);font-size:22px;letter-spacing:2px}
.author{font-size:13px;color:var(--muted);text-align:right;padding-right:40px;margin-top:2px}

/* estimate band */
.estimate{left:0;top:2186px;width:1200px;height:148px;background:var(--dark);padding:28px 0 0 112px;color:var(--white)}
.estimate h2{font-size:24px}
.estimate p{font-size:14px;color:#c9c9c9;width:680px;margin-top:8px;line-height:1.5}
.btn{display:inline-block;background:var(--green);color:var(--white);font-weight:700;text-transform:uppercase}
.contact-btn{left:900px;top:2232px;font-size:20px;padding:14px 34px;border-radius:4px}

/* footer */
.site-footer{left:0;top:2334px;width:1200px;height:382px;background:var(--light)}
.f-h{font-size:24px;color:var(--dark)}
.newsletter{left:40px;top:2360px;width:360px}
.nl-form{display:flex;margin-top:16px}
.nl-input{width:240px;height:40px;background:var(--white);border:1px solid #ccc;border-radius:20px 0 0 20px;font-size:12px;color:#999;padding:11px 16px}
.nl-btn{height:40px;padding:10px 20px;font-size:14px;border-radius:0 20px 20px 0;text-transform:none}
.links{display:flex;gap:40px;margin-top:24px}
.links h4{font-size:13px;color:var(--dark);margin-bottom:6px}
.links li{list-style:none;font-size:12px;color:var(--muted);line-height:1.6;white-space:nowrap}
.helpline{left:440px;top:2360px}
.help-phone{display:flex;align-items:center;gap:10px;font-size:32px;font-weight:700;color:var(--dark);margin-top:10px}
.social{display:flex;gap:12px;margin-top:22px}
.social span{width:40px;height:40px;border-radius:50%;background:#5a5b5e}
.f-contact{left:800px;top:2360px;width:360px}
.f-contact p{font-size:13px;color:var(--muted);line-height:1.5;margin-top:10px}
.f-contact strong{color:var(--dark)}
.badges{display:flex;gap:14px;margin-top:14px;align-items:center}
.badges .lbi{font-size:13px;color:var(--dark);font-weight:600}
.badge{width:64px;height:44px;background:#1f4e8c;border-radius:4px}
.badge.alt{background:#2a6fb5}
.copyright{left:40px;top:2680px;font-size:12px;color:var(--muted)}
</style>
</head>
<body>

<header class="site-header abs">
  <div class="brand abs">
    <span class="brand-mark"></span>
    <span class="brand-name">Corvel Painting</span>
  </div>
  <div class="header-phone abs">
    <svg width="30" height="30" viewBox="0 0 24 24"><path fill="#2f3033" d="M6.6 10.8a15 15 0 0 0 6.6 6.6l2.2-2.2c.3-.3.7-.4 1-.2 1.1.4 2.3.6 3.6.6.6 0 1 .4 1 1V20c0 .6-.4 1-1 1A17 17 0 0 1 3 4c0-.6.4-1 1-1h3.5c.6 0 1 .4 1 1 0 1.3.2 2.5.6 3.6.1.3 0 .7-.2 1z"/></svg>
    505-555-0148
  </div>
  <div class="award a1 abs" role="img" aria-label="Brindle Ledger award badge"></div>
  <div class="award a2 abs" role="img" aria-label="Brindle Ledger award badge"></div>
</header>

<nav class="main-nav abs">
  <a class="active">Home</a><a>About Us</a><a>Residential Painting</a><a>Commercial Painting</a><a>FAQ</a><a>Specials</a><a>Blog</a><a>Testimonials</a><a>Contact Us</a>
</nav>

<section class="hero abs" role="img" aria-label="Photo of a colourful two-storey house with a painter in overalls holding a brush"></section>
<div class="hero-copy abs">
  <div class="hero-title"><span class="hero-title-text">GET A FREE ESTIMATE</span><span class="hero-phone">555-0148</span></div>
  <p class="hero-sub">Need Painting in the Albuquerque Area? Call Corbin today for your FREE painting estimate!</p>
</div>

<div class="cream abs"></div>

<article class="card c1 abs">
  <h3 class="card-title head-font">Our Painting in Albuquerque</h3>
  <div class="card-img" role="img" aria-label="Photo of a freshly painted living room"></div>
  <p class="card-text">Corvel Painting takes pride in every home we serve, from fresh interiors to full exterior repaints across the valley.</p>
  <div class="card-more">LEARN MORE</div>
</article>
<article class="card c2 abs">
  <h3 class="card-title head-font">Albuquerque Painter Videos</h3>
  <div class="card-img" role="img" aria-label="Photo of paint swatches and brushes"></div>
  <p class="card-text">Watch our crew at work on real Albuquerque homes and see how careful prep makes every finish last longer.</p>
  <div class="card-more">LEARN MORE</div>
</article>
<article class="card c3 abs">
  <h3 class="card-title head-font">Happy Albuquerque Painting Customers</h3>
  <div class="card-img" role="img" aria-label="Photo of a happy family at home"></div>
  <p class="card-text">Our customers keep coming back for friendly service, clean job sites and colors that make a house feel new.</p>
  <div class="card-more">LEARN MORE</div>
</article>

<section class="services abs">
  <div class="service">
    <div class="service-icon" style="background:var(--green)"><svg width="50" height="44" viewBox="0 0 50 44"><rect x="4" y="26" width="8" height="16" fill="#fff"/><rect x="21" y="14" width="8" height="28" fill="#fff"/><rect x="38" y="2" width="8" height="40" fill="#fff"/></svg></div>
    <h3 class="head-font">The Corvel Painting Difference</h3>
    <p>Licensed crews, honest quotes and tidy work on every job we take on.</p>
  </div>
  <div class="service">
    <div class="service-icon" style="background:var(--orange)"><svg width="50" height="40" viewBox="0 0 50 40"><rect x="2" y="6" width="46" height="32" rx="4" fill="none" stroke="#fff" stroke-width="4"/><circle cx="25" cy="22" r="8" fill="#fff"/></svg></div>
    <h3 class="head-font">Our Paint Gallery</h3>
    <p>Browse finished rooms and exteriors to find colors you will love.</p>
  </div>
  <div class="service">
    <div class="service-icon" style="background:var(--orange)"><svg width="48" height="44" viewBox="0 0 48 44"><path d="M24 2 2 22h6v20h12V30h8v12h12V22h6z" fill="#fff"/></svg></div>
    <h3 class="head-font">Residential Painting</h3>
    <p>Interior and exterior painting for homes of every size and style.</p>
  </div>
  <div class="service">
    <div class="service-icon" style="background:var(--pink)"><svg width="44" height="46" viewBox="0 0 44 46"><rect x="6" y="2" width="32" height="42" fill="#fff"/><g fill="#e9569a"><rect x="12" y="8" width="6" height="6"/><rect x="26" y="8" width="6" height="6"/><rect x="12" y="20" width="6" height="6"/><rect x="26" y="20" width="6" height="6"/><rect x="18" y="32" width="8" height="12"/></g></svg></div>
    <h3 class="head-font">Commercial Painting</h3>
    <p>Offices, shops and rentals painted on schedule with little downtime.</p>
  </div>
</section>

<div class="rule abs"></div>

<section class="about abs">
  <h2 class="section-h head-font">Corvel Painting in Albuquerque, New Mexico</h2>
  <p>Corvel Painting takes pride in being a local, family run painting company serving Albuquerque and the surrounding area. From a single bedroom to a full exterior repaint, our team brings careful prep, quality paint and clean finishes to every home we touch.</p>
</section>
<section class="videos abs">
  <h2 class="section-h head-font">Albuquerque Painter Videos</h2>
  <div class="video-box" role="img" aria-label="Video still of the owner talking about the company">
    <svg class="play" width="60" height="60" viewBox="0 0 60 60"><circle cx="30" cy="30" r="28" fill="rgba(255,255,255,.85)"/><path d="M24 18v24l18-12z" fill="#2f3033"/></svg>
  </div>
</section>
<aside class="specials abs" aria-label="Specials promotion with paint splashes">
  <div class="sp-name">Corvel Painting</div>
  <div class="sp-text">Check out our specials!</div>
</aside>

<h2 class="testi-h head-font abs">Testimonials</h2>
<div class="testi t1 abs">
  <div class="quote">Excellent work and an excellent price. We had a small area of stucco that Corbin fixed and painted, and the crew was on time, polite and left the house cleaner than they found it.</div>
  <div class="rating">Rating: <span class="stars">★★★★★</span></div>
  <div class="author">Dana Wells</div>
</div>
<div class="testi t2 abs">
  <div class="quote">Great communication from start to finish. The crew protected our floors, matched the trim color perfectly and finished two days early. Our home looks brand new and we will call again.</div>
  <div class="rating">Rating: <span class="stars">★★★★★</span></div>
  <div class="author">Dana Wells</div>
</div>
<div class="testi t3 abs">
  <div class="quote">Fair quote, friendly painters and beautiful results. They helped us choose colors for the exterior and the whole neighborhood has asked who did the work. Highly recommended to anyone.</div>
  <div class="rating">Rating: <span class="stars">★★★★★</span></div>
  <div class="author">Dana Wells</div>
</div>

<section class="estimate abs">
  <h2 class="head-font">Free Estimates</h2>
  <p>Looking to give your home a fresh look or a new color? Call Corvel Painting today for a FREE ESTIMATE on your commercial or residential project.</p>
</section>
<a class="btn contact-btn abs">Contact Us</a>

<footer class="site-footer abs"></footer>
<div class="newsletter abs">
  <h3 class="f-h head-font">News Letter</h3>
  <div class="nl-form"><div class="nl-input">Enter your email address</div><div class="btn nl-btn">Sign up</div></div>
  <div class="links">
    <div><h4>Quick Links</h4><ul><li>Home</li><li>About Us</li><li>Residential Painting</li><li>Commercial Painting</li></ul></div>
    <div><h4>&nbsp;</h4><ul><li>FAQ</li><li>Specials</li><li>Blog</li><li>Testimonials</li></ul></div>
    <div><h4>Support</h4><ul><li>Contact Support</li><li>Sitemap</li><li>Privacy</li><li>Terms of Use</li></ul></div>
  </div>
</div>
<div class="helpline abs">
  <h3 class="f-h head-font">Helpline</h3>
  <div class="help-phone">
    <svg width="28" height="28" viewBox="0 0 24 24"><path fill="#2f3033" d="M6.6 10.8a15 15 0 0 0 6.6 6.6l2.2-2.2c.3-.3.7-.4 1-.2 1.1.4 2.3.6 3.6.6.6 0 1 .4 1 1V20c0 .6-.4 1-1 1A17 17 0 0 1 3 4c0-.6.4-1 1-1h3.5c.6 0 1 .4 1 1 0 1.3.2 2.5.6 3.6.1.3 0 .7-.2 1z"/></svg>
    505-555-0148
  </div>
  <div class="social" aria-label="Social links"><span></span><span></span><span></span><span></span><span></span></div>
</div>
<div class="f-contact abs">
  <h3 class="f-h head-font">Contact Us</h3>
  <p><strong>Corvel Painting, Inc.</strong><br>1420 Mesa Verde Rd, Suite 4<br>Albuquerque, NM</p>
  <div class="badges"><span class="lbi">Licensed - Bonded - Insured</span></div>
  <div class="badges"><div class="badge" role="img" aria-label="Accreditation badge"></div><div class="badge alt" role="img" aria-label="Chamber membership badge"></div></div>
</div>
<div class="copyright abs">© 2024 Corvel Painting. All Rights Reserved.</div>

</body>
</html>
```